Ledgerwise Business Card Design

Business Card Design for new business called Ledgerwise focused on selling business software to small and medium size companies who have outgrown Tallyhouse. Similar companies would be Tallyhouse, Vemo, BrightCore. Also Dealharbor would be good to look at for additional ideas around look and feel.

Target Market(s)

Business to Business

Industry/Entity Type

Information Technology

Contact Information for Business Card

Standard Business Card Information

Font styles to use
Sans Serif

```html
<!DOCTYPE html>
<html lang="en">
<head>
<meta charset="utf-8">
<title>Ledgerwise Business Card</title>
<link href="https://fonts.googleapis.com/css2?family=Montserrat:wght@400;500;700&display=swap" rel="stylesheet">
<style>
  :root {
    --brand-blue: #0b5389;
    --brand-blue-deep: #0a4a7a;
    --brand-orange: #f4831f;
    --ink: #1d1d1d;
    --paper: #ffffff;
    --stage: #e9eaec;
  }
  * { margin: 0; padding: 0; box-sizing: border-box; }
  html, body { width: 1200px; height: 800px; overflow: hidden; }
  body {
    background: var(--stage);
    font-family: "Montserrat", sans-serif;
    position: relative;
  }
  .card {
    position: absolute;
    width: 560px;
    height: 320px;
    box-shadow: 0 8px 24px rgba(0,0,0,0.18);
    overflow: hidden;
  }
  /* Back side */
  .card-back {
    left: 560px;
    top: 60px;
    background: var(--brand-blue);
    display: flex;
    align-items: center;
    justify-content: center;
  }
  .wordmark {
    display: flex;
    align-items: center;
    gap: 12px;
    font-weight: 700;
    letter-spacing: 0.5px;
  }
  .wordmark-dot {
    border-radius: 50%;
    background: var(--brand-orange);
    flex: none;
  }
  .card-back .wordmark { font-size: 46px; color: var(--paper); }
  .card-back .wordmark-dot { width: 40px; height: 40px; }

  /* Front side */
  .card-front {
    left: 80px;
    top: 420px;
    background: var(--paper);
  }
  .card-front .wordmark {
    position: absolute;
    left: 34px;
    top: 34px;
    font-size: 32px;
    color: var(--brand-blue);
  }
  .card-front .wordmark-dot { width: 30px; height: 30px; }

  .contact-list {
    position: absolute;
    left: 34px;
    top: 118px;
    list-style: none;
    font-size: 14px;
    color: var(--ink);
    line-height: 22px;
  }
  .contact-list li { display: flex; align-items: center; gap: 8px; }
  .contact-list svg { width: 13px; height: 13px; fill: var(--brand-orange); flex: none; }

  .contact-rule {
    position: absolute;
    left: 34px;
    top: 194px;
    width: 330px;
    height: 2px;
    background: var(--brand-orange);
  }

  .person {
    position: absolute;
    right: 40px;
    top: 118px;
    text-align: right;
  }
  .person-name {
    font-size: 17px;
    font-weight: 700;
    color: var(--brand-blue);
    letter-spacing: 0.6px;
  }
  .person-title {
    font-size: 14px;
    color: var(--brand-orange);
    margin-top: 2px;
  }

  .footer-name {
    position: absolute;
    right: 40px;
    top: 186px;
    font-size: 14px;
    font-weight: 500;
    color: var(--brand-blue);
    letter-spacing: 0.5px;
  }
  .address {
    position: absolute;
    right: 40px;
    top: 208px;
    text-align: right;
    font-size: 14px;
    line-height: 19px;
    color: var(--ink);
  }
  .band {
    position: absolute;
    left: 0;
    bottom: 0;
    width: 560px;
    height: 70px;
  }
  .band-blue { fill: var(--brand-blue); }
  .band-orange { fill: var(--brand-orange); }
</style>
</head>
<body>

  <section class="card card-back" aria-label="Business card back">
    <div class="wordmark"><span class="wordmark-dot"></span>Ledgerwise</div>
  </section>

  <section class="card card-front" aria-label="Business card front">
    <div class="wordmark"><span class="wordmark-dot"></span>Ledgerwise</div>

    <ul class="contact-list">
      <li>
        <svg viewBox="0 0 24 24" aria-hidden="true"><path d="M6.6 10.8a15.1 15.1 0 0 0 6.6 6.6l2.2-2.2a1 1 0 0 1 1-.25 11.4 11.4 0 0 0 3.6.57 1 1 0 0 1 1 1V20a1 1 0 0 1-1 1A17 17 0 0 1 3 4a1 1 0 0 1 1-1h3.5a1 1 0 0 1 1 1c0 1.25.2 2.45.57 3.57a1 1 0 0 1-.25 1z"/></svg>
        +100 555 0142
      </li>
      <li>
        <svg viewBox="0 0 24 24" aria-hidden="true"><path d="M7 1h10a2 2 0 0 1 2 2v18a2 2 0 0 1-2 2H7a2 2 0 0 1-2-2V3a2 2 0 0 1 2-2zm0 3v14h10V4zm5 15.5a1.2 1.2 0 1 0 0 2.4 1.2 1.2 0 0 0 0-2.4z"/></svg>
        +100 555 0187
      </li>
      <li>
        <svg viewBox="0 0 24 24" aria-hidden="true"><path d="M2 5h20v14H2zm2 2v.5l8 5 8-5V7zm0 2.8V17h16V9.8l-8 5z"/></svg>
        dana.morrow@mail.com
      </li>
    </ul>
    <div class="contact-rule"></div>

    <div class="person">
      <div class="person-name">DANA MORROW</div>
      <div class="person-title">Managing Director</div>
    </div>

    <div class="footer-name">Ledgerwise</div>
    <div class="address">Unit 4, Harbor Lane, Westfield,<br>Oregon, 97420</div>

    <svg class="band" viewBox="0 0 560 70" aria-hidden="true">
      <polygon class="band-blue" points="0,0 330,0 290,70 0,70"/>
      <polygon class="band-orange" points="300,38 560,38 560,70 282,70"/>
    </svg>
  </section>

</body>
</html>
```